Tarrowin Rugby Hockey Club - 2015 Sponsorship Packages

We are a local sporting club based in Tarrowin, Victoria Australia. We would like to attract potential sponsors to our club by making a professional and striking, double sided A3 cover document containing the information in the attached files.
The club colours blue, red and white and logo should be prominent, and all photos used.
Feel free to move text from the Sponsorship introductory letter and Membership packages files to suite layout & formatting.
Enjoy

Target Market(s)

Corporate and small business owners in local and Melbourne community

Industry/Entity Type

Club

Font styles to use
Serif

Colors
0255a3
ec2027
ffffff

Requirements
Must have
• 4 pages. 2 fold
Nice to have
• Use red white and blue colours, club logo, photos set behind text

```html
<!DOCTYPE html>
<html lang="en">
<head>
<meta charset="utf-8">
<title>Tarrowin Rugby Hockey Club – Sponsorship</title>
<link href="https://fonts.googleapis.com/css2?family=Titillium+Web:wght@300;400;600;700&family=Archivo+Black&family=Arimo:wght@700&display=swap" rel="stylesheet">
<style>
  :root {
    --club-blue: #0255a3;
    --club-blue-deep: #1a4f9c;
    --club-red: #ec2027;
    --white: #ffffff;
    --ink: #141414;
    --fold: #7fb0d8;
  }
  * { box-sizing: border-box; margin: 0; padding: 0; }
  html, body { width: 1200px; height: 848px; overflow: hidden; background: var(--white); }
  .spread { position: relative; width: 1200px; height: 848px; overflow: hidden; font-family: "Titillium Web", sans-serif; color: var(--ink); }

  .backdrop { position: absolute; top: 0; height: 766px; }
  .backdrop--inside {
    left: 0; width: 596px;
    background:
      linear-gradient(90deg, rgba(255,255,255,.72) 0%, rgba(255,255,255,.55) 45%, rgba(255,255,255,.25) 70%, rgba(255,255,255,0) 100%),
      linear-gradient(180deg, rgba(255,255,255,0) 55%, rgba(255,255,255,.95) 82%, #fff 100%),
      radial-gradient(ellipse 90px 140px at 340px 120px, rgba(60,80,170,.75), rgba(60,80,170,0) 100%),
      radial-gradient(ellipse 70px 90px at 380px 160px, rgba(220,60,70,.55), rgba(220,60,70,0) 100%),
      radial-gradient(ellipse 110px 150px at 300px 470px, rgba(40,70,160,.8), rgba(40,70,160,0) 100%),
      radial-gradient(ellipse 80px 100px at 360px 430px, rgba(215,150,130,.8), rgba(215,150,130,0) 100%),
      radial-gradient(ellipse 130px 120px at 180px 400px, rgba(200,140,120,.6), rgba(200,140,120,0) 100%),
      radial-gradient(ellipse 150px 110px at 120px 560px, rgba(50,70,150,.55), rgba(50,70,150,0) 100%),
      linear-gradient(180deg, #c9c6c4 0%, #d8cfc9 30%, #b9b9bd 55%, #e4e0dc 75%, #fff 100%);
  }
  .backdrop--cover {
    left: 597px; width: 603px;
    background:
      linear-gradient(180deg, rgba(255,255,255,0) 0%, rgba(255,255,255,0) 62%, rgba(255,255,255,.85) 80%, #fff 100%),
      linear-gradient(90deg, rgba(255,255,255,.55) 0%, rgba(255,255,255,.25) 35%, rgba(255,255,255,0) 55%),
      radial-gradient(ellipse 60px 55px at 415px 305px, rgba(200,80,70,.85), rgba(200,80,70,0) 100%),
      radial-gradient(ellipse 80px 120px at 305px 190px, rgba(60,90,190,.85), rgba(60,90,190,0) 100%),
      radial-gradient(ellipse 70px 35px at 305px 210px, rgba(225,70,80,.8), rgba(225,70,80,0) 100%),
      radial-gradient(ellipse 60px 100px at 495px 200px, rgba(60,90,190,.75), rgba(60,90,190,0) 100%),
      radial-gradient(ellipse 55px 30px at 495px 220px, rgba(225,70,80,.7), rgba(225,70,80,0) 100%),
      radial-gradient(ellipse 60px 60px at 300px 90px, rgba(225,185,150,.9), rgba(225,185,150,0) 100%),
      radial-gradient(ellipse 55px 55px at 500px 100px, rgba(220,180,150,.8), rgba(220,180,150,0) 100%),
      radial-gradient(ellipse 50px 80px at 300px 330px, rgba(240,240,245,.9), rgba(240,240,245,0) 100%),
      linear-gradient(180deg, #b7bfb2 0%, #c5c9bd 25%, #b3bb9f 45%, #a9b58c 60%, #cfd4c2 75%, #fff 100%);
  }

  .fold { position: absolute; left: 596px; top: 0; height: 848px; border-left: 1.5px dotted var(--fold); }

  .letter { position: absolute; left: 25px; top: 48px; width: 262px; font-size: 12.2px; line-height: 19px; font-weight: 400; white-space: nowrap; }
  .letter p { margin-bottom: 19px; }
  .contacts { position: absolute; left: 25px; top: 615px; font-size: 12.2px; line-height: 18px; font-weight: 400; }
  .contacts .row { display: flex; font-size: 13px; }
  .contacts .row span:first-child { width: 81px; }
  .president { position: absolute; left: 25px; top: 705px; font-size: 13px; font-weight: 400; }
  .president b { font-weight: 700; }

  .tile { position: absolute; border: 4px solid var(--club-blue-deep); overflow: hidden; }
  .tile .photo { position: absolute; inset: 0; }
  .tile .label { position: absolute; color: var(--white); font-weight: 700; font-size: 13px; line-height: 13px; text-shadow: 0 0 3px rgba(0,0,0,.8); }
  .label--top { left: 6px; top: 5px; }
  .label--bottom { left: 6px; bottom: 6px; }
  .label--right { right: 8px; bottom: 8px; }

  .club-name { position: absolute; left: 622px; top: 46px; width: 160px; display: flex; align-items: center; gap: 8px; color: var(--club-blue); font-family: "Arimo", sans-serif; font-weight: 700; font-size: 15px; line-height: 18px; }
  .club-name .dot { flex: none; width: 22px; height: 22px; border-radius: 50%; background: var(--club-red); }

  .headline { position: absolute; left: 625px; top: 261px; font-family: "Arimo", sans-serif; font-weight: 700; color: var(--club-blue-deep); text-shadow: 1px 1px 0 #fff, -1px -1px 0 #fff, 1px -1px 0 #fff, -1px 1px 0 #fff, 2px 2px 3px rgba(0,0,0,.35); }
  .headline .acronym { font-family: "Archivo Black", sans-serif; font-size: 50px; line-height: 52px; letter-spacing: 1px; }
  .headline .line { font-size: 26px; line-height: 34px; -webkit-text-stroke: .6px var(--club-blue-deep); }
  .headline .line small { font-size: 17px; }
  .headline .mission { margin-top: 2px; font-size: 17.5px; line-height: 27px; letter-spacing: .4px; -webkit-text-stroke: .5px var(--club-blue-deep); }

  .stripes { position: absolute; left: 0; width: 1200px; }
  .stripe-blue-top { top: 766px; height: 8px; background: var(--club-blue-deep); }
  .stripe-red { top: 774px; height: 14px; background: var(--club-red); }
  .stripe-blue-thin { top: 788px; height: 4px; background: var(--club-blue-deep); }
  .stripe-blue-base { top: 806px; height: 42px; background: var(--club-blue-deep); }
</style>
</head>
<body>
<main class="spread">
  <div class="backdrop backdrop--inside" role="img" aria-label="Faded photo of netballers and supporters celebrating in club colours"></div>
  <div class="backdrop backdrop--cover" role="img" aria-label="Faded action photo of footballers chasing the ball on the ground"></div>

  <section class="letter">
    <p>Season 2014 was very successful for the TRHC,<br>with 6 of our 8 sides making the finals including<br>our Senior Football side who were defeated by<br>Kelbrook with the last kick of the game in the<br>Preliminary final. Our Reserves side finished 3rd<br>and our U/18s finished a gallant runners up to<br>Kelbrook. This was a wonderful effort after so<br>many of this young side were elevated to the<br>senior team during the year, fulfilling our focus<br>on player development. Our netballers continued<br>to perform strongly. Our A Grade and U17 teams<br>both reached Preliminary finals losing by 4 goals<br>and 1 goal respectively. The A Reserve team<br>won their first final but were eliminated in the<br>1st Semi Final.</p>
    <p>Our club continues to "Punch above its' weight"<br>to consistently produce excellent results. This has<br>been largely due to the outstanding culture,<br>leadership and dedication of all associated with<br>our club. As a town and community we can be<br>very proud of our achievements. Our teams in<br>both football and netball are made up of almost<br>entirely local talent from our Tarrowin junior<br>football and netball programs as opposed to<br>many other clubs who recruit heavily from<br>outside their district. We are committed to giving<br>our local players every opportunity to represent<br>our town and community.</p>
  </section>

  <section class="contacts">
    <div>For More Information:&nbsp; TRHC Sponsorship Team</div>
    <div class="row"><span>Owen Marsh</span><span>0400 118 245</span></div>
    <div class="row"><span>Liam Carver</span><span>0400 552 817</span></div>
    <div class="row"><span>Reid Fallon</span><span>0400 903 664</span></div>
  </section>
  <div class="president"><b>Grant Ellery</b> - President</div>

  <figure class="tile" style="left:408px;top:15px;width:168px;height:168px">
    <div class="photo" role="img" aria-label="Netball players in climbing helmets at an outdoor adventure day" style="background:radial-gradient(ellipse 70px 40px at 80px 95px,#2b2f55,rgba(43,47,85,0)),radial-gradient(ellipse 80px 35px at 80px 140px,#1f2340,rgba(31,35,64,0)),linear-gradient(180deg,#7fb2e4 0%,#a9c8e6 28%,#b79a74 48%,#3a3d58 70%,#c8a47a 100%)"></div>
    <figcaption class="label label--top">Personal<br>Development</figcaption>
  </figure>
  <figure class="tile" style="left:408px;top:203px;width:168px;height:167px">
    <div class="photo" role="img" aria-label="Club members cooking at a community barbecue stall" style="background:radial-gradient(ellipse 50px 25px at 50px 45px,#e0b79a,rgba(224,183,154,0)),radial-gradient(ellipse 80px 45px at 60px 90px,#2f3f8f,rgba(47,63,143,0)),radial-gradient(ellipse 70px 30px at 110px 115px,#6a5a4a,rgba(106,90,74,0)),linear-gradient(180deg,#8c8a82 0%,#b8b2a4 22%,#34468e 50%,#2a2a32 78%,#1c1c22 100%)"></div>
    <figcaption class="label label--bottom">Community</figcaption>
  </figure>
  <figure class="tile" style="left:408px;top:390px;width:168px;height:168px">
    <div class="photo" role="img" aria-label="Club representatives shaking hands at a professional club's stadium" style="background:radial-gradient(ellipse 40px 30px at 40px 55px,#d8a98c,rgba(216,169,140,0)),radial-gradient(ellipse 40px 30px at 90px 75px,#d8a98c,rgba(216,169,140,0)),radial-gradient(ellipse 90px 40px at 60px 125px,#2d48a8,rgba(45,72,168,0)),linear-gradient(135deg,#5a3f8a 0%,#7a58a8 35%,#3a56b0 65%,#23264a 100%)"></div>
    <figcaption class="label label--top">Professional</figcaption>
  </figure>
  <figure class="tile" style="left:408px;top:578px;width:168px;height:168px">
    <div class="photo" role="img" aria-label="Senior team lined up arm in arm before a match" style="background:linear-gradient(90deg,rgba(0,0,0,0) 0%,rgba(220,60,70,.35) 20%,rgba(0,0,0,0) 40%,rgba(220,60,70,.35) 60%,rgba(0,0,0,0) 80%),linear-gradient(180deg,#7fa65a 0%,#5c7f3c 25%,#c89a80 40%,#2f4fa8 58%,#e04552 70%,#2f4fa8 82%,#7f8a5a 100%)"></div>
    <figcaption class="label label--top">Teamwork</figcaption>
  </figure>

  <div class="club-name"><span class="dot"></span><span>Tarrowin Rugby Hockey Club</span></div>

  <h1 class="headline">
    <div class="acronym">TRHC</div>
    <div class="line">STRIVING <small>FOR</small></div>
    <div class="line">SUSTAINED</div>
    <div class="line">SUCCESS</div>
    <div class="mission">by developing<br>a culture of unity,<br>responsible leadership<br>and professionalism in the<br>Tarrowin community</div>
  </h1>

  <figure class="tile" style="left:626px;top:578px;width:170px;height:169px">
    <div class="photo" role="img" aria-label="Young local players embracing after a win" style="background:radial-gradient(ellipse 45px 40px at 50px 45px,#e2b08a,rgba(226,176,138,0)),radial-gradient(ellipse 45px 40px at 115px 40px,#d9a580,rgba(217,165,128,0)),radial-gradient(ellipse 90px 60px at 90px 125px,#2c4cb0,rgba(44,76,176,0)),linear-gradient(160deg,#4a5a30 0%,#6a7a48 30%,#a08060 50%,#2f4cae 75%,#23274a 100%)"></div>
    <figcaption class="label label--right">Young &amp; Local</figcaption>
  </figure>
  <figure class="tile" style="left:808px;top:578px;width:169px;height:169px">
    <div class="photo" role="img" aria-label="Team running through the match-day banner" style="background:radial-gradient(ellipse 90px 25px at 80px 30px,#4a6ec0,rgba(74,110,192,0)),radial-gradient(ellipse 90px 35px at 80px 95px,#3a3a56,rgba(58,58,86,0)),linear-gradient(180deg,#dfe6f2 0%,#4a6ec0 25%,#c6d2e6 40%,#3c4a7a 58%,#6f8f4a 78%,#55772f 100%)"></div>
    <figcaption class="label label--right">Committed</figcaption>
  </figure>
  <figure class="tile" style="left:988px;top:578px;width:169px;height:169px">
    <div class="photo" role="img" aria-label="Netball team celebrating with a premiership trophy" style="background:radial-gradient(ellipse 80px 30px at 95px 50px,#e6bf9c,rgba(230,191,156,0)),radial-gradient(ellipse 90px 40px at 80px 105px,#2f4cae,rgba(47,76,174,0)),radial-gradient(ellipse 50px 25px at 40px 125px,#d63a48,rgba(214,58,72,0)),linear-gradient(180deg,#b9b7b2 0%,#d9bda3 35%,#3550a8 62%,#c43c48 80%,#6e6a70 100%)"></div>
    <figcaption class="label label--right">Successful</figcaption>
  </figure>

  <div class="stripes stripe-blue-top"></div>
  <div class="stripes stripe-red"></div>
  <div class="stripes stripe-blue-thin"></div>
  <div class="stripes stripe-blue-base"></div>

  <div class="fold"></div>
</main>
</body>
</html>
```